Oral Surgery Office Referral Form and Stationary designs.

Hi, I am a dentist/oral surgeon recently graduated and starting my own practice. Need help in designing an attractive, warm, appealing and Professional referral form (double sided), and stationary design. These will be used for Thank you notes, Professional letters, Front of a presentation folder, Notepads, envelopes, promotional products, Fax, etc... I do have a sample of a typical referral form and also have a logo as well as business card design that I will provide as a base to use. I will attach the files to this posting. Please, do some investigating on the Oral surgery / dental specialist websites as to some of the examples of the referral forms. Thanks and feel free to respond with any questions. Look forward to the designs - having the business card designed here was a great experience.
I will attach more files to clarify / show examples.

HELLO ALL,

I JUST WENT THROUGH THE BRIEF AND REALISED THAT THERE IS A MISTAKE IN MY POSTING. 
THE WEBSITE ADDRESS SHOULD READ:
 WWW.KRELDAX.COM 
IN MY ORIGINAL POSTING IT WAS MISSING THE "M".

TRULY APOLOGIZE FOR ANY INCONVENIENCE.
THANK YOU,
GERALD

Target Market(s)

Dental Professionals and oral surgery patients.

Industry/Entity Type

Dental

Requirements
Must have
• Has to have pictures of the mouth / teeth numbers/ map with directions. Needs to be warm and appealing. If possible to have it in a format that can be easily converted to a clickable one online. Don't know if possible. Thanks.
Should not have
• Typical dental designs .

```html
<!DOCTYPE html>
<html lang="en">
<head>
<meta charset="utf-8">
<title>Kreldax Oral Surgery – Referral Form</title>
<link href="https://fonts.googleapis.com/css2?family=Open+Sans:wght@400;600&display=swap" rel="stylesheet">
<style>
:root{
  --navy:#1b2f8f;
  --blue:#1d4fb5;
  --sky:#2aa9d8;
  --pale:#dff2fa;
  --rule:#bfe3f2;
  --ink:#222;
  --band-a:#0e2f9e;
  --band-b:#4a7fd6;
}
*{box-sizing:border-box;margin:0;padding:0}
html,body{width:1192px;height:1200px;overflow:hidden;background:#fff}
body{position:relative;font-family:"Open Sans",Arial,sans-serif;color:var(--navy)}
.backdrop{position:absolute;inset:0}
.brand{position:absolute;display:flex;flex-direction:column;align-items:center;color:var(--blue);font-weight:400;text-transform:lowercase;text-align:center}
.brand .mark{background:var(--blue)}
.brand-main{left:894px;top:40px;width:252px}
.brand-main .mark{width:64px;height:64px;margin-bottom:12px}
.brand-main .name{font-size:30px;line-height:1}
.brand-main .sub{font-size:30px;line-height:1.1}
.page{position:absolute;top:224px;width:545px;height:956px;background:#fff;border:1px solid var(--sky);box-shadow:6px 8px 12px rgba(0,0,0,.35)}
.page-front{left:36px}
.page-back{left:602px}
.band{position:absolute;left:0;right:0;bottom:16px;height:20px;background:linear-gradient(90deg,var(--band-a),var(--band-b) 60%,var(--band-a))}
.contact{position:absolute;font-size:13px;font-weight:600;line-height:23px;color:var(--navy);white-space:nowrap}
.front-contact{left:22px;top:20px}
.page .brand{width:150px}
.page .brand .mark{width:40px;height:40px;margin-bottom:6px}
.page .brand .name{font-size:16px;line-height:1.1}
.front-brand{left:355px;top:22px}
.field{position:absolute;left:22px;width:498px;font-size:13px;height:37px;border-bottom:2px solid var(--rule);display:flex;align-items:center}
.field .ph{position:absolute;color:#999;font-size:11px;font-weight:600}
.field .sl{position:absolute;color:#999;font-size:22px;font-weight:400;top:-6px}
.online{position:absolute;left:22px;top:444px;font-size:11.5px;font-weight:600}
.chart{position:absolute}
.chart-teeth{left:24px;top:502px;width:287px;height:207px;border:2px solid var(--sky);background:#fff;padding:8px}
.chart-teeth .fill{position:absolute;left:8px;right:8px;background:linear-gradient(#f1f4f8,#dfe5ee)}
.chart-teeth .upper{top:8px;height:78px}
.chart-teeth .lower{top:118px;height:80px}
.numrow{position:absolute;left:26px;display:flex;gap:2px}
.numrow span{width:13px;height:13px;border:1px solid var(--navy);font-size:7px;line-height:11px;text-align:center;background:#fff}
.numrow.top span{background:var(--pale)}
.chart-primary{left:361px;top:495px;width:146px;height:200px;background:radial-gradient(ellipse at center,#fff 30%,#e6ebf2 70%,#fff 100%)}
.chart-primary .lbl{position:absolute;top:92px;width:100%;text-align:center;font-size:8px;color:var(--ink);font-weight:600}
.tissue-label{position:absolute;left:22px;top:756px;font-size:8px;color:var(--ink);font-weight:600}
.chart-tissue{top:736px;width:156px;height:167px;border-radius:48% 48% 42% 42%;background:radial-gradient(ellipse at 50% 60%,#f3eded 25%,#e4e8ef 60%,#fff 100%)}
.tissue-a{left:123px}
.tissue-b{left:318px}
.h{position:absolute;font-size:12px;font-weight:600;color:var(--ink)}
.opt{position:absolute;font-size:12px;display:flex;align-items:center;gap:7px;white-space:nowrap;color:var(--navy)}
.opt::before{content:"";width:10px;height:10px;border:1.5px solid var(--sky);flex:none}
.line{position:absolute;height:1px;background:var(--sky)}
.instructions{position:absolute;left:26px;top:462px;width:494px;height:307px;border:2px solid var(--rule);padding:10px 10px;font-size:8.6px;line-height:17.5px;color:var(--sky)}
.instructions h3{font-size:8.6px;font-weight:600;color:var(--ink);line-height:14px}
.instructions .gap{height:10px}
.map{position:absolute;left:29px;top:800px;width:180px;height:103px;border:2px solid var(--rule);background:linear-gradient(135deg,#eef0f2,#d9dde2)}
.back-contact{left:218px;top:800px;font-size:10.5px;line-height:23px}
.back-brand{left:375px;top:810px}
</style>
</head>
<body>

<svg class="backdrop" width="1192" height="1200" viewBox="0 0 1192 1200" aria-hidden="true">
  <defs>
    <linearGradient id="wave" x1="0" x2="1">
      <stop offset="0" stop-color="#d5eef8"/>
      <stop offset="1" stop-color="#eaf6fb"/>
    </linearGradient>
  </defs>
  <path d="M0 0 H520 C420 60 300 140 0 150 Z" fill="#eef8fc"/>
  <path d="M380 0 C520 120 700 230 1000 270 C1100 283 1160 270 1192 250 V300 C1000 340 700 300 520 200 C440 150 400 60 380 0 Z" fill="url(#wave)"/>
  <path d="M640 0 C720 60 820 110 1000 120 C1100 125 1160 110 1192 100 V160 C1060 200 860 190 720 90 C690 60 660 30 640 0 Z" fill="#e2f3fa"/>
</svg>

<div class="brand brand-main">
  <div class="mark"></div>
  <div class="name">kreldax</div>
  <div class="sub">oral surgery</div>
</div>

<section class="page page-front">
  <div class="contact front-contact">
    2250 Linden Avenue, Harlow, NE 68000<br>
    P (402) 555 0142<br>
    F (402) 555 0147<br>
    www.kreldax.com
  </div>
  <div class="brand front-brand">
    <div class="mark"></div>
    <div class="name">kreldax<br>oral surgery</div>
  </div>

  <div class="field" style="top:171px">Today's Date
    <span class="ph" style="left:130px">DD</span><span class="sl" style="left:167px">/</span>
    <span class="ph" style="left:185px">MM</span><span class="sl" style="left:222px">/</span>
    <span class="ph" style="left:242px">YYYY</span></div>
  <div class="field" style="top:208px">Appt. date
    <span class="ph" style="left:130px">DD</span><span class="sl" style="left:167px">/</span>
    <span class="ph" style="left:185px">MM</span><span class="sl" style="left:222px">/</span>
    <span class="ph" style="left:242px">YYYY</span>
    <span style="position:absolute;left:318px">Day</span></div>
  <div class="field" style="top:245px">Time<span style="position:absolute;left:318px;font-size:12px">AM/PM</span></div>
  <div class="field" style="top:283px">Patient's Name</div>
  <div class="field" style="top:320px">Patient's Phone Number</div>
  <div class="field" style="top:358px">Referred by</div>
  <div class="field" style="top:395px;border-bottom:none">Additional Comments</div>
  <p class="online">You can save time by going online. Register and update your health history today!</p>

  <div class="chart chart-teeth">
    <div class="fill upper" role="img" aria-label="Permanent upper teeth chart"></div>
    <div class="numrow top" style="top:90px">
      <span>1</span><span>2</span><span>3</span><span>4</span><span>5</span><span>6</span><span>7</span><span>8</span><span>9</span><span>10</span><span>11</span><span>12</span><span>13</span><span>14</span><span>15</span><span>16</span>
    </div>
    <div class="numrow" style="top:104px">
      <span>32</span><span>31</span><span>30</span><span>29</span><span>28</span><span>27</span><span>26</span><span>25</span><span>24</span><span>23</span><span>22</span><span>21</span><span>20</span><span>19</span><span>18</span><span>17</span>
    </div>
    <div class="fill lower" role="img" aria-label="Permanent lower teeth chart"></div>
  </div>

  <div class="chart chart-primary" role="img" aria-label="Deciduous teeth chart, upper and lower arches lettered A to T">
    <span class="lbl">DECIDUOUS TEETH</span>
  </div>

  <span class="tissue-label">SOFT TISSUE CHART</span>
  <div class="chart chart-tissue tissue-a" role="img" aria-label="Soft tissue chart of the open mouth"></div>
  <div class="chart chart-tissue tissue-b" role="img" aria-label="Soft tissue chart of the open mouth"></div>

  <div class="band"></div>
</section>

<section class="page page-back">
  <span class="h" style="left:57px;top:36px">PROCEDURE</span>
  <span class="opt" style="left:57px;top:58px">Extraction</span>
  <span class="opt" style="left:159px;top:58px">Implants</span>
  <span class="opt" style="left:260px;top:58px">Consultation</span>
  <span class="opt" style="left:363px;top:58px">Radiographs</span>

  <span class="opt" style="left:40px;top:122px">Wisdom Teeth</span>
  <span class="opt" style="left:40px;top:145px">Extraction</span>
  <span class="opt" style="left:40px;top:167px">Implants</span>
  <span class="opt" style="left:40px;top:190px">Bone Grafting</span>
  <span class="opt" style="left:40px;top:212px">Exposure and bonding</span>
  <span class="opt" style="left:40px;top:235px">Biopsy(SOFT or Hard Tissue)</span>

  <span class="opt" style="left:232px;top:122px">Lesion Evaluation</span>
  <span class="opt" style="left:232px;top:145px">Infection (I&amp;D)</span>
  <span class="opt" style="left:232px;top:167px">Alveoloplasty</span>
  <span class="opt" style="left:232px;top:190px">Frenectomy</span>
  <span class="opt" style="left:232px;top:212px">Orthognathic</span>
  <span class="opt" style="left:232px;top:235px">TMJ</span>
  <span class="opt" style="left:232px;top:258px">Other</span>
  <span class="line" style="left:248px;top:283px;width:88px"></span>
  <span class="line" style="left:248px;top:302px;width:88px"></span>

  <span class="h" style="left:368px;top:122px">Implants</span>
  <span class="opt" style="left:368px;top:145px">Corvel</span>
  <span class="opt" style="left:368px;top:167px">Tessan</span>
  <span class="opt" style="left:368px;top:190px">Alden</span>
  <span class="opt" style="left:368px;top:212px">Vyre</span>
  <span class="opt" style="left:368px;top:235px">Other</span>
  <span class="line" style="left:388px;top:262px;width:88px"></span>
  <span class="line" style="left:388px;top:282px;width:88px"></span>

  <span class="h" style="left:46px;top:308px">Surgical Template</span>
  <span class="opt" style="left:18px;top:329px">To be provided by Restorative dentist</span>
  <span class="opt" style="left:325px;top:329px">To be fabricated by the surgeon</span>
  <span class="opt" style="left:18px;top:350px">Other</span>
  <span class="line" style="left:102px;top:364px;width:140px"></span>

  <span class="h" style="left:46px;top:385px">Radiographs</span>
  <span class="opt" style="left:18px;top:405px">Being Mailed/emailed</span>
  <span class="opt" style="left:205px;top:405px">Given to the Patient</span>
  <span class="opt" style="left:380px;top:405px">Please Take</span>
  <span class="opt" style="left:18px;top:426px">Other</span>
  <span class="line" style="left:102px;top:441px;width:140px"></span>

  <div class="instructions">
    <h3>Patient Instructions</h3>
    <p>PLEASE NOTE THAT IN MOST INSTANCES THE PATIENT IS FIRST SEEN FOR CONSULTATION TO REVIEW THE HEALTH HISTORY; DECIDE ON THE MOST APPROPRIATE ANESTHESIA AND TREATMENT PLAN, AND SCHEDULE THE SURGERY AT A SEPARATE APPOINTMENT.</p>
    <p>Please assist us by having the following information available with you at the time of appointment: Your surgical referral slip and any x-rays if applicable, a list of medications, insurance policy information.</p>
    <p>IMPORTANT: All patients unmarried or under the age of 19 must be accompanied by a Parent or guardian during the Consultation and Treatment visits.</p>
    <div class="gap"></div>
    <p>SPECIAL INSTRUCTIONS FOR PATIENTS HAVING I.V. SEDATION / GENERAL ANESTHESIA:</p>
    <p>&nbsp;&nbsp;&nbsp;- NO FOOD OR DRINK (including WATER) AT LEAST 6 HOURS PRIOR TO YOUR SURGERY UNLESS OTHERWISE INDICATED BY THE SURGEON. Some medications may be continued and this will be discussed at your consultation.</p>
    <p>&nbsp;&nbsp;&nbsp;- A responsible adult must accompany you and REMAIN in the office during the entire treatment. They must also be able to drive you home. YOU cannot drive until the next day.</p>
    <p>&nbsp;&nbsp;&nbsp;- Eat a light and easily digestible meal the night before the procedure. Do not drink any alcoholic beverages the night before.</p>
    <p>&nbsp;&nbsp;&nbsp;- Wear comfortable clothing with sleeves which are easy to push up.</p>
  </div>

  <div class="map" role="img" aria-label="Street map showing the office location"></div>
  <div class="contact back-contact">
    2250 Linden Avenue, Harlow, NE 68000<br>
    P (402) 555 0142<br>
    F (402) 555 0147<br>
    www.kreldax.com
  </div>
  <div class="brand back-brand">
    <div class="mark"></div>
    <div class="name">kreldax<br>oral surgery</div>
  </div>

  <div class="band"></div>
</section>

</body>
</html>
```